Business Card- Occupational Therapist

I need business cards for Tallowood KinderMove, I am an Occupational Therapist offering child centred play therapy.
I am a sole private practitioner offering play therapy services to families in rural Great Southern region of WA, my mission statement is "helping rural children and communities thrive"
This is a new business so I am needing to promote the value of child centred play therapy within the community, and my referrers (target audience) will be: rural GPs (doctors), child health nurse, schools, disability providers, child protection workers etc) but also the families of young children in rural areas.
Target Market(s)
Families of children
Referrers (Doctors, child health nurse, schools, disability providers, child protection workers)
Industry/Entity Type
Mental Health
Contact Information for Business Card
Mira Toveland
Occupational Therapist
Phone: 0487 552 019
Email: mira@tkmove.com.au
PO Box 71 | WENDARRIN 6421
Requirements
Must have
- Include Tallowood KinderMove logo and my contact details.
Include my credentials as an Occupational Therapist and Child Centred Play Therapist
Nice to have
- "Play is a child's language and toys are their words" Delbert Quorin

```html
<!DOCTYPE html>
<html lang="en">
<head>
<meta charset="utf-8">
<title>Tallowood KinderMove – Business Cards</title>
<link rel="stylesheet" href="https://fonts.googleapis.com/css2?family=Quicksand:wght@400;500;700&display=swap">
<style>
  :root{
    --stage:#2a2a2c;
    --card-front:#efefef;
    --card-back:#ffffff;
    --green:#2ea836;
    --purple:#6b1f6e;
    --ink:#2b2b2b;
    --ghost-front:#e4e4e4;
    --ghost-back:#f2f8f1;
  }
  *{box-sizing:border-box;margin:0;padding:0}
  html,body{width:1200px;height:900px;overflow:hidden}
  body{background:var(--stage);font-family:"Quicksand",sans-serif;color:var(--ink);position:relative}
  .card{position:absolute;left:290px;width:620px;height:354px;overflow:hidden;box-shadow:0 10px 30px rgba(0,0,0,.45)}
  .card--front{top:62px;background:var(--card-front);border-left:4px solid var(--green);border-right:4px solid var(--purple)}
  .card--back{top:484px;background:var(--card-back);border-left:4px solid var(--green);border-bottom:4px solid var(--purple)}
  .ghost-mark{position:absolute;border-radius:50%}
  .card--front .ghost-mark{width:300px;height:300px;right:-40px;top:70px;background:var(--ghost-front)}
  .card--back .ghost-mark{width:300px;height:300px;right:40px;top:90px;background:var(--ghost-back)}
  .brand{position:absolute;display:flex;align-items:center;gap:14px}
  .brand__name{font-weight:400;font-size:26px;line-height:1.15;letter-spacing:.5px;color:var(--ink)}
  .brand__dot{width:46px;height:46px;border-radius:50%;background:var(--green);flex:none}
  .card--front .brand{left:150px;top:58px}
  .card--back .brand{left:40px;top:34px}
  .card--back .brand__name{font-size:22px}
  .card--back .brand__dot{width:40px;height:40px}
  .credentials{position:absolute;left:150px;top:196px;font-size:15px;line-height:1.5;font-weight:500}
  .person{position:absolute;left:40px;top:142px}
  .person__name{font-weight:700;font-size:21px;color:var(--purple)}
  .person__role{font-size:19px;margin-top:2px}
  .contacts{position:absolute;left:40px;top:222px;list-style:none;font-size:13px;font-weight:700}
  .contacts li{display:flex;align-items:center;gap:10px;margin-bottom:8px}
  .contacts svg{width:16px;height:16px;flex:none;fill:var(--purple)}
</style>
</head>
<body>
  <section class="card card--front">
    <div class="ghost-mark"></div>
    <div class="brand">
      <span class="brand__dot"></span>
      <span class="brand__name">Tallowood<br>KinderMove</span>
    </div>
    <p class="credentials">Occupational Therapist and<br>Child Centred Play Therapist</p>
  </section>

  <section class="card card--back">
    <div class="ghost-mark"></div>
    <div class="brand">
      <span class="brand__dot"></span>
      <span class="brand__name">Tallowood<br>KinderMove</span>
    </div>
    <div class="person">
      <p class="person__name">Mira Toveland</p>
      <p class="person__role">Occupational Therapist</p>
    </div>
    <ul class="contacts">
      <li><svg viewBox="0 0 24 24"><path d="M6.6 10.8a15 15 0 0 0 6.6 6.6l2.2-2.2a1 1 0 0 1 1-.25 11.4 11.4 0 0 0 3.6.57 1 1 0 0 1 1 1V20a1 1 0 0 1-1 1A17 17 0 0 1 3 4a1 1 0 0 1 1-1h3.5a1 1 0 0 1 1 1c0 1.25.2 2.45.57 3.57a1 1 0 0 1-.25 1z"/></svg>Phone: 0487 552 019</li>
      <li><svg viewBox="0 0 24 24"><path d="M2 5h20v14H2z M3 6l9 7 9-7" stroke="#fff" stroke-width="1.5"/></svg>Email: mira@tkmove.com.au</li>
      <li><svg viewBox="0 0 24 24"><path d="M12 2a7 7 0 0 0-7 7c0 5 7 13 7 13s7-8 7-13a7 7 0 0 0-7-7zm0 9.5A2.5 2.5 0 1 1 12 6.5a2.5 2.5 0 0 1 0 5z"/></svg>PO Box 71 | WENDARRIN 6421</li>
    </ul>
  </section>
</body>
</html>
```